Brolvane Co.,Ltd. need business card

Brolvane Company Limited is a facility management company. We provides a total solution services from administration, energy saving, security, safety, food catering to companies.

The logo should be in elegant style with innovative that suited to the upper market
Please see the logo image in the attached file. You can use this Red or Blue or Green checkerboard (color and font should be similar to logo) as the main part of business card (can be an entire of one side of business card) . In another side of card should contain contact details of personnel - here below demo information

Kanyarat Thoengsai
Chief Executive Officer

No.73, Soi 5, Ruam Wongsa Road
Nong Khaem, Bangkok,
10520, Thailand

Tel + 66841537296
Mobile + 66841537296
E-mail: Kanyarat.Thoengsai@brolvane-example.co.th

Target Market(s)

Factory, Hotel and Hospital

Industry/Entity Type

Business

Contact Information for Business Card

Kanyarat Thoengsai
Chief Executive Officer

Nong Khaem, Bangkok,
10520, Thailand

Tel + 66841537296
Mobile + 66841537296

We will change details with the winner designer

Font styles to use
Sans Serif

Requirements
Must have
• In style of red checkerboard and white color

```html
<!DOCTYPE html>
<html lang="en">
<head>
<meta charset="utf-8">
<title>Brolvane Co.,Ltd. — Business Card</title>
<link rel="stylesheet" href="https://fonts.googleapis.com/css2?family=PT+Sans:ital,wght@0,400;0,700;1,400&display=swap">
<style>
  :root {
    --brand-red: #e30613;
    --pattern-red: #ea6a6f;
    --pattern-light: #f3b9bb;
    --card-grey: #e5e5e5;
    --page-white: #ffffff;
    --ink: #1a1a1a;
  }
  * { margin: 0; padding: 0; box-sizing: border-box; }
  html, body {
    width: 1200px; height: 1000px; overflow: hidden;
    background: var(--page-white);
    font-family: "PT Sans", Arial, sans-serif;
    color: var(--ink);
  }
  .canvas { position: relative; width: 1200px; height: 1000px; }

  .card {
    position: absolute;
    width: 549px; height: 377px;
    background: var(--card-grey);
    box-shadow: 4px 5px 8px rgba(0,0,0,0.35);
    overflow: hidden;
  }
  .card--front { left: 196px; top: 107px; }
  .card--back  { left: 406px; top: 495px; height: 376px; }

  .pattern-area {
    position: absolute;
    background: linear-gradient(135deg, var(--pattern-red), var(--pattern-light) 50%, var(--pattern-red));
  }
  .card--front .band-top    { left: 0; top: 0; width: 549px; height: 141px; }
  .card--front .band-bottom { left: 0; top: 268px; width: 549px; height: 109px; }

  .wordmark {
    position: absolute; left: 0; top: 141px; width: 549px; height: 127px;
    display: flex; align-items: center; justify-content: center;
    font-weight: 400; font-size: 88px; letter-spacing: 1px;
    color: var(--brand-red); line-height: 1;
  }

  .corner { width: 62px; }
  .corner--tl { left: 0; top: 0; height: 141px; }
  .corner--tr { right: 0; top: 0; height: 141px; }
  .corner--bl { left: 0; bottom: 0; height: 109px; }
  .corner--br { right: 0; bottom: 0; height: 109px; }

  .dots { position: absolute; left: 239px; display: flex; gap: 5px; }
  .dots span { width: 6px; height: 6px; background: var(--brand-red); }
  .dots--top { top: 33px; }
  .dots--bottom { top: 338px; }

  .person { position: absolute; left: 94px; top: 137px; }
  .person-name { font-weight: 700; font-size: 16px; line-height: 20px; }
  .person-title { font-style: italic; font-size: 13px; line-height: 16px; }

  .divider {
    position: absolute; left: 252px; top: 140px;
    width: 2px; height: 129px; background: var(--brand-red);
  }

  .contact { position: absolute; left: 266px; font-size: 10px; line-height: 12.5px; }
  .contact-icon { position: absolute; left: -20px; top: 0; }
  .contact--address { top: 169px; }
  .contact--address .contact-icon { top: 10px; }
  .contact--phone { top: 214px; }
  .contact--phone .contact-icon { top: 4px; }
  .contact--email { top: 247px; }
  .contact--email .contact-icon { top: 2px; }
</style>
</head>
<body>
<main class="canvas">

  <section class="card card--front" aria-label="Card front">
    <div class="pattern-area band-top" role="img" aria-label="Red and white checkerboard band"></div>
    <div class="wordmark">BROLVANE</div>
    <div class="pattern-area band-bottom" role="img" aria-label="Red and white checkerboard band"></div>
  </section>

  <section class="card card--back" aria-label="Card back">
    <div class="pattern-area corner corner--tl" role="img" aria-label="Red and white checkerboard corner strip"></div>
    <div class="pattern-area corner corner--tr" role="img" aria-label="Red and white checkerboard corner strip"></div>
    <div class="pattern-area corner corner--bl" role="img" aria-label="Red and white checkerboard corner strip"></div>
    <div class="pattern-area corner corner--br" role="img" aria-label="Red and white checkerboard corner strip"></div>

    <div class="dots dots--top"><span></span><span></span><span></span></div>
    <div class="dots dots--bottom"><span></span><span></span><span></span></div>

    <div class="person">
      <p class="person-name">Kanyarat Thoengsai</p>
      <p class="person-title">Chief Executive Officer</p>
    </div>

    <div class="divider"></div>

    <div class="contact contact--address">
      <svg class="contact-icon" width="11" height="13" viewBox="0 0 11 13" aria-hidden="true">
        <path d="M5.5 0.8a4.3 4.3 0 0 0-4.3 4.3c0 3.2 4.3 7.3 4.3 7.3s4.3-4.1 4.3-7.3A4.3 4.3 0 0 0 5.5 0.8z" fill="none" stroke="#e30613" stroke-width="1.4"/>
        <circle cx="5.5" cy="5.1" r="1.5" fill="#e30613"/>
      </svg>
      <p>No.73, Soi 5, Ruam Wongsa Road</p>
      <p>Nong Khaem, Bangkok,</p>
      <p>10520, Thailand</p>
    </div>

    <div class="contact contact--phone">
      <svg class="contact-icon" width="11" height="11" viewBox="0 0 24 24" aria-hidden="true">
        <path fill="#e30613" d="M6.6 10.8a15.1 15.1 0 0 0 6.6 6.6l2.2-2.2c.3-.3.7-.4 1-.2 1.1.4 2.3.6 3.6.6.6 0 1 .4 1 1V20c0 .6-.4 1-1 1A17 17 0 0 1 3 4c0-.6.4-1 1-1h3.5c.6 0 1 .4 1 1 0 1.3.2 2.5.6 3.6.1.3 0 .7-.2 1z"/>
      </svg>
      <p>Tel + 66841537296</p>
      <p>Mobile + 66841537296</p>
    </div>

    <div class="contact contact--email">
      <svg class="contact-icon" width="13" height="9" viewBox="0 0 13 9" aria-hidden="true">
        <rect x="0" y="0" width="13" height="9" fill="#e30613"/>
        <path d="M0.5 0.5 L6.5 5 L12.5 0.5" fill="none" stroke="#e5e5e5" stroke-width="1"/>
      </svg>
      <p>E-mail: Kanyarat.Thoengsai@brolvane-example.co.th</p>
    </div>
  </section>

</main>
</body>
</html>
```